Harbinger Noble Alloys Works Business Cards

We are wanting to have a new business card designed for our company as we go to a convention. We want to balance business/Modern with elegance and beauty. Our company sells highend jewelry pieces. We want to utilize the colors of Black and Gold and have gold foiled fonts to be physically printed on the business cards.
We also would like to have space to write notes on the back side of the business card. When we meet people at jewelry conventions we would like to write notes if possible.
Here are websites and designs that we like the look and feel of these companies and you can use these as design ideas.
https://www.lorvanne.com
https://www.bellquist.com/en-us/home
Here is our company website link
www.harbingernaw.com
I also up loaded two versions of our logo.
- Update 4.26.22
I have uploaded photos of a business card we like. this card has raised embossed letters that you can feel. the raise letters are like a plastic but we don't need to use that...I uploaded to show you that we like the experience of the client feeling the characters of the logo. we also would like to have the material as a satin or some material very soft.
- Maybe we can get designs with beautiful gold foiling and raised characters and logos. we like simplicity...not busy but an elegant design. We need to write notes and would like a section where we can write notes. but we want an elegant style and the client has an experience with the feel of the card when they touch the card.
Colors
- Main colors Black & Gold
- white or light colors for small notes section.
Specialty ideals and things we would like to see based on your design styles.
- raised fonts
- raised logos
- gold foiling
- satin/soft finish on the card material.
we are wanting to design a business card that looks elegant and clean. When the client is handed the business card we want them to physically experience the business card as well by touching the raised logos or fonts and the base material is soft satin. I hope this helps with further designs.
thank you all
We uploaded a new contact layout that we have designed in our office. we would like to see how this would look on your designs.
thank you
I just finished uploading the Contact Layout. the colors are just examples. please use this layout as an idea and use colors based on the feed back we have given each of you personally.
Contact Information for Business Card
we need an area to write notes, we would like to have our logos or the diamond of our logo or the business card to have embossed sections to the business card so when the customer touches the card they can feel the logo. we would also like sections of our business card to have gold foiling. we would also like to use a satin soft paper with our card. when the client touches the card its super soft and high quality
Requirements
Must have
- we would like to have our logos or the diamond of our logo or the business card to have embossed sections to the business card so when the customer touches the card they can feel the logo. we would also like sections of our business card to have gold foiling. we would also like to use a satin soft paper with our card. when the client touches the card its super soft and high quality
Nice to have
- we would like to have our logos or the diamond of our logo or the business card to have embossed sections to the business card so when the customer touches the card they can feel the logo. we would also like sections of our business card to have gold foiling.

```html
<!DOCTYPE html>
<html lang="en">
<head>
<meta charset="utf-8">
<title>Harbinger Noble Alloys Works — Business Cards</title>
<link rel="stylesheet" href="https://fonts.googleapis.com/css2?family=Cinzel:wght@400;500&family=Cormorant+Garamond:wght@400;500&display=swap">
<style>
  :root {
    --canvas: #e9e6e1;
    --card-black: #0d0d0d;
    --band-dark: #070707;
    --band-light: #1a1a1a;
    --gold: #c99a34;
    --gold-soft: #a9833a;
    --gold-line: #d8aa48;
    --notes-paper: #f3eee4;
    --notes-rule: #d9ccb0;
  }
  html, body {
    margin: 0;
    padding: 0;
    width: 1200px;
    height: 1200px;
    overflow: hidden;
    background: var(--canvas);
  }
  .sheet {
    width: 1200px;
    height: 1200px;
    display: flex;
    flex-direction: column;
    align-items: center;
    justify-content: center;
    gap: 44px;
  }
  .card {
    position: relative;
    width: 880px;
    height: 533px;
    background: var(--card-black);
    box-shadow: 0 6px 18px rgba(0,0,0,0.25);
    overflow: hidden;
  }
  .card-stripes {
    position: absolute;
    inset: 0;
    width: 100%;
    height: 100%;
  }
  .brand-mark {
    position: absolute;
    border-radius: 50%;
    background: var(--gold);
  }
  .front-mark {
    left: 424px;
    top: 204px;
    width: 32px;
    height: 32px;
  }
  .front-wordmark {
    position: absolute;
    left: 0;
    right: 0;
    top: 248px;
    margin: 0;
    text-align: center;
    font-family: "Cinzel", serif;
    font-weight: 400;
    font-size: 24px;
    letter-spacing: 0.5px;
    color: var(--gold);
  }
  .holder {
    position: absolute;
    left: 74px;
    top: 72px;
  }
  .holder-name {
    margin: 0;
    font-family: "Cinzel", serif;
    font-weight: 500;
    font-size: 28px;
    color: var(--gold);
  }
  .holder-title {
    margin: 6px 0 0;
    font-family: "Cormorant Garamond", serif;
    font-size: 12px;
    letter-spacing: 1.5px;
    color: var(--gold-soft);
  }
  .notes-area {
    position: absolute;
    left: 74px;
    top: 150px;
    width: 470px;
    height: 220px;
    background: var(--notes-paper);
    background-image: repeating-linear-gradient(to bottom, transparent 0, transparent 43px, var(--notes-rule) 43px, var(--notes-rule) 44px);
    border: 1px solid var(--gold-soft);
    box-sizing: border-box;
  }
  .back-brand {
    position: absolute;
    left: 640px;
    top: 312px;
    display: flex;
    align-items: center;
    gap: 10px;
    margin: 0;
    font-family: "Cormorant Garamond", serif;
    font-weight: 500;
    font-size: 14px;
    color: var(--gold);
  }
  .back-mark {
    position: static;
    width: 18px;
    height: 18px;
    flex: none;
  }
  .contact-list {
    position: absolute;
    left: 670px;
    top: 370px;
    margin: 0;
    padding: 0;
    list-style: none;
    font-family: "Cormorant Garamond", serif;
    font-size: 11.5px;
    line-height: 1.3;
    color: var(--gold-soft);
  }
  .contact-item {
    display: flex;
    align-items: center;
    gap: 20px;
    margin-bottom: 18px;
  }
  .contact-icon {
    width: 14px;
    height: 14px;
    flex: none;
    fill: var(--gold);
  }
</style>
</head>
<body>
<main class="sheet">

  <section class="card card-front" aria-label="Card front">
    <svg class="card-stripes" viewBox="0 0 880 533" aria-hidden="true">
      <polygon points="600,0 880,0 880,165" fill="var(--band-dark)"/>
      <polygon points="700,0 880,0 880,100" fill="var(--band-light)"/>
      <line x1="600" y1="0" x2="880" y2="165" stroke="var(--gold-line)" stroke-width="1.2"/>
      <line x1="740" y1="0" x2="880" y2="80" stroke="var(--gold-line)" stroke-width="1.2"/>
      <line x1="830" y1="0" x2="880" y2="28" stroke="var(--gold-line)" stroke-width="1"/>
      <polygon points="0,360 0,533 300,533" fill="var(--band-dark)"/>
      <polygon points="0,440 0,533 160,533" fill="var(--band-light)"/>
      <line x1="0" y1="360" x2="300" y2="533" stroke="var(--gold-line)" stroke-width="1.2"/>
      <line x1="0" y1="440" x2="160" y2="533" stroke="var(--gold-line)" stroke-width="1.2"/>
      <line x1="0" y1="400" x2="230" y2="533" stroke="var(--gold-line)" stroke-width="0.8"/>
    </svg>
    <span class="brand-mark front-mark" role="img" aria-label="Company emblem, embossed"></span>
    <h1 class="front-wordmark">Harbinger Noble Alloys Works</h1>
  </section>

  <section class="card card-back" aria-label="Card back">
    <svg class="card-stripes" viewBox="0 0 880 533" aria-hidden="true">
      <polygon points="480,0 880,0 880,185" fill="var(--band-dark)"/>
      <polygon points="620,0 880,0 880,120" fill="var(--band-light)"/>
      <line x1="480" y1="0" x2="880" y2="185" stroke="var(--gold-line)" stroke-width="1.2"/>
      <line x1="640" y1="0" x2="880" y2="110" stroke="var(--gold-line)" stroke-width="1.2"/>
      <line x1="790" y1="0" x2="880" y2="42" stroke="var(--gold-line)" stroke-width="1"/>
      <polygon points="0,370 0,533 320,533" fill="var(--band-dark)"/>
      <polygon points="0,450 0,533 170,533" fill="var(--band-light)"/>
      <line x1="0" y1="370" x2="320" y2="533" stroke="var(--gold-line)" stroke-width="1.2"/>
      <line x1="0" y1="450" x2="170" y2="533" stroke="var(--gold-line)" stroke-width="1.2"/>
    </svg>

    <div class="holder">
      <h2 class="holder-name">MS XXXX</h2>
      <p class="holder-title">PROJECT MANAGER</p>
    </div>

    <div class="notes-area" role="img" aria-label="Light writing area for handwritten notes"></div>

    <p class="back-brand"><span class="brand-mark back-mark" aria-hidden="true"></span>Harbinger Noble Alloys Works</p>

    <ul class="contact-list">
      <li class="contact-item">
        <svg class="contact-icon" viewBox="0 0 16 16" aria-hidden="true"><path d="M8 1 L15 8 H13 V15 H9.5 V10.5 H6.5 V15 H3 V8 H1 Z"/></svg>
        <span>2210 Larkmoor Ave NE<br>Dunmore, Oregon USA 97390</span>
      </li>
      <li class="contact-item">
        <svg class="contact-icon" viewBox="0 0 16 16" aria-hidden="true"><circle cx="8" cy="8" r="7"/><path d="M1 8 H15 M8 1 C4 5 4 11 8 15 C12 11 12 5 8 1" stroke="#0d0d0d" stroke-width="1" fill="none"/></svg>
        <span>info@harbingernaw.com<br>www.harbingernaw.com</span>
      </li>
      <li class="contact-item">
        <svg class="contact-icon" viewBox="0 0 16 16" aria-hidden="true"><path d="M1 5 C1 3 3 2 8 2 C13 2 15 3 15 5 V6.5 H11.5 V4.8 H4.5 V6.5 H1 Z M3 8 H13 L14 14 H2 Z"/></svg>
        <span>(555) 014-2270</span>
      </li>
    </ul>
  </section>

</main>
</body>
</html>
```